Bramblewick Gardening Services. A6 flyer single sided

Need an A6 flyer designing. Single sided.
I am a gardener.
I do lawn mowing - one-off garden tidy ups or regular fortnightly visits.
All kinds of trees expertly felled, topped or pruned.
Hedge cutting.
Fencing replaced or repaired.
Fully insured.
Access to fully qualified and licenced tree arborist
07724 316048 or 01632 742918.

I have attached my business card and letter head logo.
I'm open to new designs without incorporating any of my artwork.

Industry/Entity Type

Gardener

```html
<!DOCTYPE html>
<html lang="en">
<head>
<meta charset="utf-8">
<title>Bramblewick Gardening Services – A6 Flyer</title>
<link rel="stylesheet" href="https://fonts.googleapis.com/css2?family=Cabin:ital,wght@0,500;0,600;0,700;1,500&display=swap">
<style>
  :root {
    --page-bg: #8a8b8f;
    --ink: #3d3f3f;
    --panel: rgba(245, 246, 240, 0.82);
    --green: #5a9a2a;
    --gravel: #dcdcd4;
  }
  * { box-sizing: border-box; margin: 0; padding: 0; }
  html, body {
    width: 1200px; height: 1000px; overflow: hidden;
    background: var(--page-bg);
    font-family: "Cabin", "Helvetica Neue", Arial, sans-serif;
    color: var(--ink);
  }
  .flyer {
    position: absolute; left: 296px; top: 70px;
    width: 608px; height: 860px; overflow: hidden;
    box-shadow: 0 6px 24px rgba(0,0,0,0.25);
  }
  .garden-photo {
    position: absolute; inset: 0;
    background: linear-gradient(180deg, var(--green) 0%, var(--green) 35%, var(--gravel) 50%, var(--gravel) 66%, var(--green) 82%, var(--green) 100%);
  }
  .title-panel {
    position: absolute; left: 22px; right: 22px; top: 0; height: 218px;
    background: var(--panel);
    border-radius: 0 0 30px 30px;
    text-align: right; padding: 48px 30px 0 0;
  }
  .brand-name { font-size: 48px; font-weight: 700; letter-spacing: 1px; line-height: 1; }
  .brand-line { font-size: 34px; font-weight: 600; line-height: 1.1; margin-top: 4px; }
  .brand-sub { font-size: 19px; font-weight: 600; margin-top: 8px; }
  .contact-panel {
    position: absolute; left: 248px; top: 250px; width: 318px; height: 126px;
    background: var(--panel); border-radius: 24px;
    text-align: right; padding: 14px 26px 0 0;
  }
  .contact-name { font-size: 24px; font-weight: 600; }
  .contact-phone { font-size: 29px; font-weight: 600; line-height: 1.1; letter-spacing: 1px; }
  .services {
    position: absolute; left: 70px; right: 30px; top: 420px;
    list-style: none; text-align: left;
    font-size: 23px; font-weight: 600; line-height: 1.25;
  }
  .email-panel {
    position: absolute; left: 22px; right: 22px; bottom: 0; height: 150px;
    background: var(--panel); border-radius: 30px 30px 0 0;
    display: flex; align-items: center; justify-content: center;
  }
  .email { font-size: 25px; font-style: italic; font-weight: 500; letter-spacing: 5px; }
</style>
</head>
<body>
  <main class="flyer">
    <div class="garden-photo" role="img" aria-label="Photograph of clipped box hedges beside a white gravel path"></div>

    <header class="title-panel">
      <h1 class="brand-name">BRAMBLEWICK</h1>
      <p class="brand-line">Gardening Services</p>
      <p class="brand-sub">&amp; Exterior Property Maintenance</p>
    </header>

    <section class="contact-panel">
      <p class="contact-name">Rob Ashcombe</p>
      <p class="contact-phone">07724 316048</p>
      <p class="contact-phone">01632 742918</p>
    </section>

    <ul class="services">
      <li>Regular Visits or 1 Off Garden Tidy-Ups</li>
      <li>Lawn Mowing, Pruning, Strimming</li>
      <li>Fencing - Installation, Painting or Repairs</li>
      <li>Jet Washing Drives, Pations, etc</li>
    </ul>

    <footer class="email-panel">
      <p class="email">bramblewick@mailbox.com</p>
    </footer>
  </main>
</body>
</html>
```